Business Card Design Project

I need a new business card design for my building/development company: Ridgewell Constructions.

We specialise in small sub-divisions, multi-story developments and new house builds.
We handle the whole process from concept stage right throught to a fully developed property.
Updates

Project Deadline Extended
Reason: Need a couple of extra days to decide as there are so many amazing designs

Target Market(s)

people looking to develop their property and need help. New property buyers

Industry/Entity Type

House

Requirements
Must have
• My logo on both sides:
Side 1: Logo taking up whole side as per old card but with a color/style change.

Side 2: Contact page: include logo but the rest just surprise me!

All contact details will be: (and need to be changable for each employee) I'll inform you of specifics before printing.

Name Surname
Position ie. Managing director
M: insert mobile
E: insert email
P.O. Box 518, Elmhurst, Vic, 3145
www.ridgewellconstructions.com.au

Nice to have
• Colors i'd like: (not necessarily all but this is the basic idea)

Black, blue, grey, silver, white

```html
<!DOCTYPE html>
<html lang="en">
<head>
<meta charset="utf-8">
<title>Ridgewell Constructions – Business Card</title>
<link href="https://fonts.googleapis.com/css2?family=Open+Sans:wght@400;600&family=Roboto+Condensed:wght@300;400;700&display=swap" rel="stylesheet">
<style>
  :root {
    --page: #ffffff;
    --frame: #8a8a8a;
    --card-light: #f4f4f4;
    --card-light-edge: #dcdcdc;
    --cyan: #00c8ff;
    --blue: #0036ff;
    --ink: #1a1a1a;
    --ink-soft: #333333;
    --white: #ffffff;
    --silver-top: #f2f2f2;
    --silver-bottom: #b4b4b4;
  }
  * { margin: 0; padding: 0; box-sizing: border-box; }
  html, body { width: 967px; height: 1200px; overflow: hidden; background: var(--page); }
  .sheet { position: relative; width: 967px; height: 1200px; border: 1px solid var(--frame); }

  .card { position: absolute; left: 29px; width: 910px; overflow: hidden; border: 1px solid #777; }
  .card--front {
    top: 39px; height: 541px;
    background: radial-gradient(ellipse at center, #ffffff 30%, var(--card-light) 70%, var(--card-light-edge) 100%);
  }
  .card--back {
    top: 615px; height: 544px;
    background: linear-gradient(180deg, var(--cyan) 0%, #0a8cff 40%, var(--blue) 100%);
    border-color: #3a6cff;
  }

  .side-bar { position: absolute; width: 33px; }
  .side-bar--blue { background: linear-gradient(180deg, var(--cyan), var(--blue)); top: 27px; height: 488px; }
  .side-bar--silver { background: linear-gradient(180deg, var(--silver-top), var(--silver-bottom)); top: 28px; height: 488px; width: 27px; }
  .side-bar--left { left: 0; border-radius: 0 8px 8px 0; }
  .side-bar--right { right: 0; border-radius: 8px 0 0 8px; }

  .brand-name { font-family: "Open Sans", sans-serif; font-weight: 600; white-space: nowrap; }
  .brand-mark { display: block; background: var(--cyan); }

  .front-brand { position: absolute; left: 0; right: 0; top: 150px; text-align: center; }
  .front-brand .brand-mark { width: 150px; height: 150px; margin: 0 auto 18px; }
  .front-brand .brand-name { font-size: 46px; line-height: 56px; color: var(--ink); letter-spacing: -0.5px; }
  .front-brand .tagline {
    font-family: "Open Sans", sans-serif; font-size: 20px; color: var(--ink-soft);
    margin-top: 2px; letter-spacing: 0.3px;
  }
  .front-url {
    position: absolute; left: 0; right: 0; top: 480px; text-align: center;
    font-family: "Open Sans", sans-serif; font-size: 19px; letter-spacing: 3.5px; color: #444;
  }

  .back-brand { position: absolute; left: 50px; top: 50px; color: var(--white); }
  .back-brand .brand-mark { width: 68px; height: 68px; margin: 0 0 10px 48px; background: #6fdcff; }
  .back-brand .brand-name { font-size: 22px; line-height: 28px; color: var(--white); }
  .back-brand .tagline { font-family: "Open Sans", sans-serif; font-size: 10px; margin-left: 10px; }

  .person { position: absolute; right: 47px; top: 68px; text-align: right; color: var(--white); font-family: "Roboto Condensed", sans-serif; }
  .person .name { font-weight: 700; font-size: 31px; line-height: 34px; }
  .person .role { font-weight: 300; font-size: 26px; line-height: 30px; }

  .contact { position: absolute; left: 50px; top: 372px; color: var(--white); font-family: "Roboto Condensed", sans-serif; font-weight: 300; font-size: 26px; line-height: 30.5px; }
  .contact li { list-style: none; display: flex; }
  .contact .label { width: 48px; font-weight: 700; }
</style>
</head>
<body>
<div class="sheet">
  <section class="card card--front">
    <div class="side-bar side-bar--blue side-bar--left"></div>
    <div class="side-bar side-bar--blue side-bar--right"></div>
    <div class="front-brand">
      <span class="brand-mark"></span>
      <div class="brand-name">Ridgewell Constructions</div>
      <div class="tagline">renovation-construction-development</div>
    </div>
    <div class="front-url">www.ridgewellconstructions.com.au</div>
  </section>

  <section class="card card--back">
    <div class="side-bar side-bar--silver side-bar--left"></div>
    <div class="side-bar side-bar--silver side-bar--right"></div>
    <div class="back-brand">
      <span class="brand-mark"></span>
      <div class="brand-name">Ridgewell Constructions</div>
      <div class="tagline">renovation-construction-development</div>
    </div>
    <div class="person">
      <div class="name">Marcus Delaney</div>
      <div class="role">Managing director</div>
    </div>
    <ul class="contact">
      <li><span class="label">M :</span><span>0400 555 218</span></li>
      <li><span class="label">&nbsp;E :</span><span>ridgewell@corenet.com.au</span></li>
      <li><span class="label"></span><span>P.O. Box 518, Elmhurst, Vic, 3145</span></li>
      <li><span class="label"></span><span>www.ridgewellconstructions.com.au</span></li>
    </ul>
  </section>
</div>
</body>
</html>
```